Mobile Web App Design for Wellness Company

We already do have a website design developed at this address:
http://new.fernbrookwellnessllc.com/

We need mobile web design. Not a mobile application design. We need design for what visitors would see when they visit http://new.fernbrookwellnessllc.com/ on their mobile phones.

Mobile Web App design need to be similar to design of the actual website, please check from the address.

We need design for below pages:
- Home
- Biodynamic Craniosacral Therapy
- Biodynamic Lymphatic Drainage
- Chi Gong
- Contact Us
- About Us

We want easy access and obvious locations for navigate and call functionality.

We put together a design for mobile already but it's not good. Feel free to take the content from the website and/or mobile web app we designed to show your design with the actual content.

Design files must be high quality. We want designer to encorporate header images for the actual website we placed into mobile pages. For example, there's a header photo for each services, when visited in mobile, we'd like those images to show up too.

Most important part of this design will be easy of use and minimalist mobile focused design.

Good Luck!

Industry/Entity Type

Health And Wellness

Number of Pages Required

5+ page

Requirements
Must have
• Most important part of this design will be easy of use and minimalist mobile focused design.
Nice to have
• New up to date looking calming design
Should not have
• Dark background color

```html
<!DOCTYPE html>
<html lang="en">
<head>
<meta charset="utf-8">
<title>Fernbrook Wellness – Contact Us</title>
<link rel="stylesheet" href="https://fonts.googleapis.com/css2?family=Great+Vibes&family=Lora:wght@700&family=Open+Sans:wght@400;600;700&display=swap">
<style>
  :root {
    --brand-blue: #0d5797;
    --icon-blue: #1a5fa0;
    --ink: #3d3d3d;
    --body-ink: #444444;
    --field-bg: #e1e4e8;
    --topbar-bg: #f0f0f0;
    --topbar-icon: #8a8a8a;
    --rule-grey: #bdbdbd;
    --rule-teal: #4aa39b;
    --white: #ffffff;
  }
  * { box-sizing: border-box; margin: 0; padding: 0; }
  html, body { width: 1200px; height: 3930px; overflow: hidden; }
  body { position: relative; background: var(--white); font-family: "Open Sans", Arial, sans-serif; color: var(--body-ink); }

  .topbar { position: absolute; left: 0; top: 0; width: 1200px; height: 122px; background: var(--topbar-bg); border-bottom: 3px solid #dddddd; }
  .topbar svg { position: absolute; top: 41px; }
  .topbar .social-dot { position: absolute; right: 50px; top: 44px; width: 34px; height: 34px; border-radius: 50%; background: var(--topbar-icon); }

  .site-header { position: absolute; left: 0; top: 122px; width: 1200px; height: 278px; }
  .brand-name { position: absolute; left: 44px; top: 100px; font-family: "Open Sans", Arial, sans-serif; font-weight: 600; font-size: 54px; color: var(--icon-blue); letter-spacing: 0.5px; }
  .menu-toggle { position: absolute; left: 1027px; top: 75px; width: 122px; height: 122px; border-radius: 50%; border: 3px solid #555; display: flex; align-items: center; justify-content: center; }

  .hero { position: absolute; left: 0; top: 400px; width: 1200px; height: 519px;
    background: linear-gradient(180deg, #6f8fb3 0%, #a9bfd6 30%, #d4dde6 48%, #2d4f8f 58%, #8b8f95 72%, #cfc9c0 84%, #6c7a8c 100%); }
  .hero-title { position: absolute; left: 0; width: 100%; top: 170px; text-align: center; font-family: "Great Vibes", cursive; font-weight: 400; font-size: 140px; letter-spacing: 6px; word-spacing: 20px; color: var(--white); text-shadow: 0 2px 8px rgba(0,0,0,0.35); }

  .section-title { position: absolute; left: 44px; font-family: "Lora", Georgia, serif; font-weight: 700; font-size: 58px; color: var(--ink); }

  .field { position: absolute; left: 46px; width: 1108px; background: var(--field-bg); font-size: 43px; color: var(--body-ink); padding: 30px 52px; }
  .field-name { top: 1232px; height: 131px; }
  .field-email { top: 1406px; height: 131px; }
  .field-message { top: 1580px; height: 293px; }

  .send-button { position: absolute; left: 38px; top: 1911px; width: 1125px; height: 151px; border-radius: 76px; background: var(--brand-blue); color: var(--white); font-weight: 700; font-size: 46px; letter-spacing: 1px; display: flex; align-items: center; justify-content: center; }

  .rule { position: absolute; left: 46px; width: 1108px; height: 3px; }
  .rule-grey { top: 2188px; background: var(--rule-grey); }
  .rule-teal { top: 3217px; height: 5px; background: var(--rule-teal); }

  .info-row { position: absolute; left: 46px; width: 1108px; display: flex; align-items: center; }
  .info-icon { width: 152px; height: 152px; border-radius: 50%; border: 3px solid #666; display: flex; align-items: center; justify-content: center; flex-shrink: 0; }
  .info-text { margin-left: 63px; font-size: 43px; line-height: 78px; color: var(--body-ink); }
  .row-address { top: 2467px; }
  .row-phone { top: 2699px; }
  .row-email { top: 2931px; }

  .footer-brand { position: absolute; left: 0; width: 100%; top: 3432px; text-align: center; font-weight: 600; font-size: 60px; color: var(--icon-blue); }
  .footer-line { position: absolute; left: 0; width: 100%; text-align: center; font-size: 38px; color: var(--body-ink); }
  .copyright { top: 3622px; }
  .tagline { top: 3712px; }
</style>
</head>
<body>
  <div class="topbar">
    <svg style="left:46px" width="40" height="40" viewBox="0 0 24 24"><path fill="#8a8a8a" d="M6.6 10.8c1.4 2.8 3.8 5.1 6.6 6.6l2.2-2.2c.3-.3.7-.4 1-.2 1.1.4 2.3.6 3.6.6.6 0 1 .4 1 1V20c0 .6-.4 1-1 1C10.6 21 3 13.4 3 4c0-.6.4-1 1-1h3.5c.6 0 1 .4 1 1 0 1.3.2 2.5.6 3.6.1.3 0 .7-.2 1z"/></svg>
    <svg style="left:190px" width="54" height="40" viewBox="0 0 27 20"><rect x="0" y="0" width="27" height="20" rx="2" fill="#8a8a8a"/><path d="M1 2l12.5 9L26 2" fill="none" stroke="#f0f0f0" stroke-width="2"/></svg>
    <span class="social-dot"></span>
  </div>

  <header class="site-header">
    <div class="brand-name">Fernbrook Wellness</div>
    <div class="menu-toggle">
      <svg width="46" height="40" viewBox="0 0 46 40"><rect y="2" width="46" height="7" rx="3" fill="#1a5fa0"/><rect y="17" width="46" height="7" rx="3" fill="#1a5fa0"/><rect y="32" width="46" height="7" rx="3" fill="#1a5fa0"/></svg>
    </div>
  </header>

  <section class="hero" role="img" aria-label="Photo of balanced smooth stones by a calm lake under a blue cloudy sky">
    <h1 class="hero-title">Contact Us</h1>
  </section>

  <h2 class="section-title" style="top:1062px">Contact Us</h2>
  <div class="field field-name">Name</div>
  <div class="field field-email">Email</div>
  <div class="field field-message">Message</div>
  <div class="send-button">SEND MESSAGE</div>

  <div class="rule rule-grey"></div>

  <h2 class="section-title" style="top:2290px">Contact Information</h2>

  <div class="info-row row-address">
    <div class="info-icon">
      <svg width="40" height="56" viewBox="0 0 20 28"><path fill="#1a5fa0" d="M10 0C4.5 0 0 4.4 0 9.8 0 17 10 28 10 28s10-11 10-18.2C20 4.4 15.5 0 10 0zm0 14a4.2 4.2 0 1 1 0-8.4 4.2 4.2 0 0 1 0 8.4z"/></svg>
    </div>
    <div class="info-text">412 Maple Grove Avenue,<br>Suite 110, Brookhaven, IL 60512</div>
  </div>

  <div class="info-row row-phone">
    <div class="info-icon">
      <svg width="50" height="50" viewBox="0 0 24 24"><path fill="#1a5fa0" d="M6.6 10.8c1.4 2.8 3.8 5.1 6.6 6.6l2.2-2.2c.3-.3.7-.4 1-.2 1.1.4 2.3.6 3.6.6.6 0 1 .4 1 1V20c0 .6-.4 1-1 1C10.6 21 3 13.4 3 4c0-.6.4-1 1-1h3.5c.6 0 1 .4 1 1 0 1.3.2 2.5.6 3.6.1.3 0 .7-.2 1z"/></svg>
    </div>
    <div class="info-text">555-214-7730</div>
  </div>

  <div class="info-row row-email">
    <div class="info-icon">
      <svg width="62" height="46" viewBox="0 0 27 20"><rect x="0" y="0" width="27" height="20" rx="2" fill="#1a5fa0"/><path d="M1 2l12.5 9L26 2" fill="none" stroke="#ffffff" stroke-width="2"/></svg>
    </div>
    <div class="info-text">info@fernbrookwellnessllc.com</div>
  </div>

  <div class="rule rule-teal"></div>

  <footer>
    <div class="footer-brand">Fernbrook Wellness</div>
    <p class="footer-line copyright">2017, Fernbrook Wellness LLC. All Rights Reserved.</p>
    <p class="footer-line tagline">Guiding you toward lasting calm, balance and daily wellness</p>
  </footer>
</body>
</html>
```